Tidal Fern Business Cards

We need something new, fun and exciting for business cards. Our current ones are just plain and we need a design that pops. We want name, position held, phone, email on the front, and a 20% discount on the back. I have also uploaded our old business cards creative to see what we are not wanting, and how boring they were and we want something jazzed up from this, cool design and catches people attention.

```html
<!DOCTYPE html>
<html lang="en">
<head>
<meta charset="utf-8">
<title>Tidal Fern Business Cards</title>
<link href="https://fonts.googleapis.com/css2?family=Poppins:wght@400;500;600;700;800&display=swap" rel="stylesheet">
<style>
  :root {
    --navy: #1b4377;
    --navy-deep: #173762;
    --pattern-light: #4a85d2;
    --pattern-mid: #2f63ab;
    --pattern-dark: #1c4683;
    --coral: #ef6f6c;
    --coral-soft: #f6a9a6;
    --white: #ffffff;
    --stage: #e9e6e3;
  }
  * { box-sizing: border-box; margin: 0; padding: 0; }
  html, body { width: 1200px; height: 649px; overflow: hidden; }
  body {
    background: var(--stage);
    font-family: "Poppins", Arial, sans-serif;
    position: relative;
  }
  .card {
    position: absolute;
    width: 540px;
    height: 310px;
    border-radius: 18px;
    overflow: hidden;
    box-shadow: 0 10px 24px rgba(0,0,0,.18);
  }

  /* Back of card */
  .card-back { left: 45px; top: 170px; background: var(--navy); }
  .card-back .pattern-area {
    position: absolute; inset: 0;
    background:
      radial-gradient(circle at 20% 30%, rgba(90,150,230,.55) 0%, transparent 45%),
      radial-gradient(circle at 75% 75%, rgba(60,120,200,.45) 0%, transparent 45%),
      linear-gradient(135deg, var(--pattern-light) 0%, var(--pattern-mid) 45%, var(--pattern-dark) 100%);
  }
  .offer-band {
    position: absolute; left: 60px; top: 110px;
    width: 420px; height: 88px;
    display: flex;
    border-radius: 8px; overflow: hidden;
  }
  .offer-brand {
    width: 150px; background: var(--coral);
    display: flex; align-items: center; justify-content: center;
    color: var(--white); font-weight: 700; font-size: 20px;
  }
  .offer-text {
    flex: 1; background: var(--navy-deep);
    display: flex; flex-direction: column; justify-content: center;
    padding-left: 22px; color: var(--white); line-height: 1;
  }
  .offer-value { font-size: 50px; font-weight: 800; letter-spacing: -1px; }
  .offer-label { font-size: 25px; font-weight: 700; letter-spacing: 1px; margin-top: 4px; }
  .back-url {
    position: absolute; left: 0; right: 0; bottom: 28px;
    text-align: center; font-size: 14px; font-weight: 500; color: var(--coral);
  }
  .back-url strong { color: var(--white); font-weight: 700; }

  /* Front of card */
  .card-front { left: 615px; top: 170px; background: var(--navy); }
  .card-front .graphic-area {
    position: absolute; left: 175px; top: 0; right: 0; bottom: 0;
    background: radial-gradient(ellipse 70% 75% at 62% 50%, var(--white) 0%, var(--white) 55%, var(--coral-soft) 78%, var(--coral) 100%);
  }
  .brand {
    position: absolute; left: 300px; top: 100px;
    display: flex; flex-direction: column; align-items: flex-start;
  }
  .brand-line { display: flex; align-items: center; gap: 10px; }
  .brand-dot { width: 24px; height: 24px; border-radius: 50%; background: var(--coral); }
  .brand-name { font-size: 36px; font-weight: 600; color: var(--navy); line-height: 1; }
  .brand-tag {
    margin-left: 34px; margin-top: 6px;
    font-size: 9.5px; font-weight: 700; letter-spacing: 1px; color: var(--navy);
  }
  .person { position: absolute; left: 30px; top: 188px; color: var(--white); }
  .person-name { font-size: 17px; font-weight: 600; color: var(--coral); line-height: 1.2; }
  .person-role { font-size: 13px; font-weight: 600; margin-bottom: 14px; }
  .contact-list { list-style: none; font-size: 12.5px; line-height: 16px; }
  .contact-list li { display: flex; align-items: center; gap: 8px; }
  .contact-list svg { width: 10px; height: 10px; fill: var(--coral); flex: none; }
</style>
</head>
<body>

<section class="card card-back">
  <div class="pattern-area" role="img" aria-label="Repeating decorative brand pattern in light and dark blue"></div>
  <div class="offer-band">
    <div class="offer-brand">Tidal Fern</div>
    <div class="offer-text">
      <span class="offer-value">20%</span>
      <span class="offer-label">DISCOUNT</span>
    </div>
  </div>
  <p class="back-url">www.<strong>tidalfern</strong>.com</p>
</section>

<section class="card card-front">
  <div class="graphic-area" role="img" aria-label="Large decorative brand graphic in coral and white"></div>
  <div class="brand">
    <div class="brand-line">
      <span class="brand-dot"></span>
      <span class="brand-name">Tidal Fern</span>
    </div>
    <span class="brand-tag">CANNABIS DISPENSARY</span>
  </div>
  <div class="person">
    <p class="person-name">Daniel Reyes</p>
    <p class="person-role">President</p>
    <ul class="contact-list">
      <li><svg viewBox="0 0 10 10" aria-hidden="true"><path d="M2 0 L4 2.5 L3 3.8 C3.6 5 5 6.4 6.2 7 L7.5 6 L10 8 L8.5 10 C4 10 0 6 0 1.5 Z"/></svg>415-555-0182</li>
      <li><svg viewBox="0 0 10 10" aria-hidden="true"><path d="M0 1.5 H10 V8.5 H0 Z"/><path d="M0 1.5 L5 5.5 L10 1.5" fill="none" stroke="var(--navy)" stroke-width="1"/></svg>hello@tidalfern.com</li>
      <li><svg viewBox="0 0 10 10" aria-hidden="true"><circle cx="5" cy="5" r="5"/></svg>www.tidalfern.com</li>
    </ul>
  </div>
</section>

</body>
</html>
```